Brent Sowle Director / Photographer Branding

I need note pads, envelops, business cards and letter head for my company. I'm a fashion and advertising director / photographer. I'm having trouble deciding how to include both Director & Photographer in my title or if it is even necessary. Maybe just my name is enough. I'm open for even using my initials if it works with the design and overall pieces. Please view my website to see what I have at this moment and what work I do. www.brentsowle.example
Updates

Project Deadline Extended
Reason: Hello Everyone! I'm extending the deadline since I have been traveling on a job out of country and I wanted to have more time to look through all the designs and give enough time for everyone to provide changes with designs and updates. I will be more available to communicate online now that I'm back in the office! Thank you! Brent Sowle

Target Market(s)

Fashion magazines, clothing lines and beauty cosmetic brands.

Industry/Entity Type

Fashion Photography

Font styles to use
Sans Serif

Colors
acd036
acd35d
cbcbcb
f5f5f5

Requirements
Must have
• My name.. Brent Sowle, my website: brentsowle.example my phone number, 555-284-6031
• I don't need my address on these. I also live by the philosophy that less is more and keeping things simple ads strength to a design. I also don't want to stop people from taking chances and experimenting with an idea that might take me down different road with my branding.
Nice to have
• Bold designs and clean lines. I'm open to ideas that I could adopt but I lean towards a more minimalistic look in general.
Should not have
• Not have cheesy graphics or pictures. No images of cameras, film or anything that looks like it is a camera or aperture, lens etc... ;)

```html
<!DOCTYPE html>
<html lang="en">
<head>
<meta charset="utf-8">
<title>Brent Sowle — Stationery Set</title>
<link href="https://fonts.googleapis.com/css2?family=Inter:wght@400&family=Montserrat:wght@400&display=swap" rel="stylesheet">
<style>
  :root {
    --backdrop: #d8d8d8;
    --charcoal: #36333a;
    --charcoal-edge: #2c2a30;
    --paper: #ffffff;
    --lime: #8fc641;
    --ink: #555459;
    --muted: #bdbbc0;
    --caption: #6f6f6f;
  }
  * { margin: 0; padding: 0; box-sizing: border-box; }
  html, body { width: 1200px; height: 951px; overflow: hidden; }
  body {
    background: var(--backdrop);
    font-family: "Inter", sans-serif;
    position: relative;
  }
  .piece { position: absolute; overflow: hidden; }
  .dark { background: var(--charcoal); }
  .light { background: var(--paper); }

  .name-set {
    position: absolute;
    color: var(--lime);
    font-weight: 400;
    line-height: 1;
    white-space: nowrap;
  }

  .url { position: absolute; left: 0; right: 0; text-align: center; color: var(--lime); font-size: 6px; letter-spacing: 0.02em; }

  /* Notepad */
  .notepad { left: 275px; top: 139px; width: 335px; height: 464px; }
  .notepad .binding { position: absolute; left: 15px; top: 0; bottom: 0; width: 1px; background: #4a474f; }
  .notepad .name-set { left: 42px; top: 50px; font-size: 20px; }
  .notepad .url { top: 427px; }

  /* Letterhead */
  .letterhead { left: 656px; top: 150px; width: 331px; height: 450px; }
  .letterhead .name-set { left: 0; right: 0; text-align: center; top: 38px; font-size: 16px; }
  .letterhead .rule { position: absolute; left: 144px; top: 402px; width: 36px; height: 1px; background: var(--lime); }
  .letterhead .contact {
    position: absolute; top: 413px; left: 0; right: 0;
    display: flex; justify-content: center; gap: 9px;
    font-size: 5px; color: var(--ink);
  }
  .contact-item { display: flex; align-items: center; gap: 3px; white-space: nowrap; }
  .contact-item svg { width: 5px; height: 5px; fill: var(--lime); flex: none; }

  /* Business cards */
  .card-front { left: 41px; top: 698px; width: 162px; height: 91px; }
  .card-front .name-set { left: 0; right: 0; text-align: center; top: 40px; font-size: 10px; }
  .card-back { left: 222px; top: 697px; width: 162px; height: 92px; }
  .card-back .name-set { left: 12px; top: 40px; font-size: 9px; }
  .card-back .details { position: absolute; left: 80px; top: 26px; font-size: 5px; line-height: 1.35; color: var(--ink); }
  .card-back .details .person { text-transform: uppercase; }
  .card-back .details .role { color: var(--lime); margin-bottom: 3px; }
  .card-caption {
    position: absolute; left: 136px; top: 805px;
    font-family: "Montserrat", sans-serif; font-size: 11px; color: var(--caption); letter-spacing: 0.02em;
  }

  /* Envelopes */
  .envelope-front { left: 427px; top: 623px; width: 329px; height: 164px; }
  .envelope-front .name-set { left: 26px; top: 32px; font-size: 11px; }
  .envelope-back { left: 646px; top: 683px; width: 331px; height: 166px; }
  .envelope-back .flap { position: absolute; inset: 0; width: 100%; height: 100%; }
  .envelope-back .url { top: 133px; color: var(--muted); font-size: 5px; }
</style>
</head>
<body>

  <section class="piece notepad dark">
    <div class="binding"></div>
    <div class="name-set">Brent Sowle</div>
    <div class="url">brentsowle.example</div>
  </section>

  <section class="piece letterhead light">
    <div class="name-set">Brent Sowle</div>
    <div class="rule"></div>
    <div class="contact">
      <span class="contact-item"><svg viewBox="0 0 10 10"><path d="M2 0h2l1 3-1.5 1a6 6 0 0 0 2.5 2.5L7 5l3 1v2c0 1-1 2-2 2A8 8 0 0 1 0 2c0-1 1-2 2-2z"/></svg>+555-284-6031</span>
      <span class="contact-item"><svg viewBox="0 0 10 10"><rect x="0" y="2" width="10" height="6"/></svg>brent@brentsowle.example</span>
      <span class="contact-item"><svg viewBox="0 0 10 10"><circle cx="5" cy="5" r="4.5"/></svg>brentsowle.example</span>
    </div>
  </section>

  <section class="piece card-front dark">
    <div class="name-set">Brent Sowle</div>
  </section>

  <section class="piece card-back light">
    <div class="name-set">Brent Sowle</div>
    <div class="details">
      <div class="person">Brent Sowle</div>
      <div class="role">Photographer/ Director</div>
      <div class="contact-item"><svg viewBox="0 0 10 10"><path d="M2 0h2l1 3-1.5 1a6 6 0 0 0 2.5 2.5L7 5l3 1v2c0 1-1 2-2 2A8 8 0 0 1 0 2c0-1 1-2 2-2z"/></svg>+555-284-6031</div>
      <div class="contact-item"><svg viewBox="0 0 10 10"><rect x="0" y="2" width="10" height="6"/></svg>brent@brentsowle.example</div>
      <div class="contact-item"><svg viewBox="0 0 10 10"><circle cx="5" cy="5" r="4.5"/></svg>www.brentsowle.example</div>
    </div>
  </section>

  <p class="card-caption">Letterpress Business Card (Grey or White)</p>

  <section class="piece envelope-front dark">
    <div class="name-set">Brent Sowle</div>
  </section>

  <section class="piece envelope-back dark">
    <svg class="flap" viewBox="0 0 331 166" preserveAspectRatio="none" aria-hidden="true">
      <polyline points="0,0 166,82 331,0" fill="none" stroke="var(--charcoal-edge)" stroke-width="1"/>
    </svg>
    <div class="url">brentsowle.example</div>
  </section>

</body>
</html>
```